Etiketten für Wein und Sekt
Zielgruppe
Sekt- und Weinherstellung
Zielgruppe 25 - 60 Jahre
Aufgabenstellung
Wir führen ein neues Produkt in den Markt ein:
gewünschter Name: The Velvet Dusk Mood
Hervorgehoben werden soll 'Velvet Dusk'
auf dieser Basis suchern wir einmal das Etikett für den WEIN
und einmal das Etikett für den SEKT (gleiches Design/Designfamilie)
Beim Sekt dachten wir an den Zusatz Sparkling auf dem Etikett?
Achtung, es handelt sich hier um keinen Eiswein !
Damit darf unser Produkt nicht in Verbindung gebracht werden (dt. Weinrecht)
Unser Wein/Sekt ist ein fruchtiger Rose Wein/Sekt
Ein Cuvée aus regionalen Rebsorten
Beim Trinkgenuss sollen die Gedanken an gefrorene Beeren/Trauben gehen.
Wir dachten an Beerentöne und Rosegold (wie der Inhalt)
Aktuell verwenden wir Etikettenformen in Rechteckgröße horizontal oder vertikal
Besten Dank im Voraus !!

```html
<!DOCTYPE html>
<html lang="de">
<head>
<meta charset="utf-8">
<title>The Velvet Dusk Mood – Wine Label</title>
<link rel="stylesheet" href="https://fonts.googleapis.com/css2?family=Source+Serif+4:wght@400&family=Playfair+Display:wght@500&family=Roboto:wght@700&family=Sacramento&display=swap">
<style>
  :root {
    --berry-base: #b36a84;
    --berry-deep: #7a0044;
    --berry-shadow: #6b2040;
    --frost-white: #fbeef3;
    --frost-pink: #e8c3d2;
    --label-white: #ffffff;
  }
  * { margin: 0; padding: 0; box-sizing: border-box; }
  html, body {
    width: 934px;
    height: 1200px;
    overflow: hidden;
    background: var(--berry-base);
  }
  .label {
    position: relative;
    width: 934px;
    height: 1200px;
    overflow: hidden;
    background: var(--berry-base);
  }
  .frost-border {
    position: absolute;
    inset: 0;
    background:
      radial-gradient(ellipse 62% 58% at 50% 50%, rgba(179,106,132,0) 62%, rgba(232,195,210,0.55) 86%, rgba(251,238,243,0.9) 100%);
  }
  .brand-banner {
    position: absolute;
    left: 268px;
    top: 0;
    width: 399px;
    height: 254px;
    background: var(--berry-deep);
    display: flex;
    align-items: flex-end;
    justify-content: center;
    padding-bottom: 50px;
  }
  .brand-name {
    font-family: "Source Serif 4", Georgia, serif;
    font-weight: 400;
    font-size: 78px;
    line-height: 1;
    color: var(--label-white);
  }
  .product-title { font-weight: normal; }
  .title-line {
    position: absolute;
    left: 0;
    width: 100%;
    text-align: center;
    line-height: 1;
  }
  .title-article {
    top: 344px;
    font-family: "Roboto", Arial, sans-serif;
    font-weight: 700;
    font-size: 76px;
    color: var(--berry-deep);
  }
  .title-highlight {
    font-family: "Playfair Display", "Times New Roman", serif;
    font-weight: 500;
    font-size: 168px;
    letter-spacing: -2px;
  }
  .title-highlight--light {
    top: 408px;
    color: var(--label-white);
    text-shadow: -7px 5px 0 var(--berry-shadow);
  }
  .title-highlight--deep {
    top: 578px;
    color: var(--berry-deep);
    text-shadow: -7px 5px 0 var(--label-white);
  }
  .title-tail {
    top: 782px;
    font-family: "Roboto", Arial, sans-serif;
    font-weight: 700;
    font-size: 64px;
    color: var(--label-white);
  }
  .wine-type {
    top: 852px;
    font-family: "Sacramento", cursive;
    font-size: 190px;
    color: var(--berry-deep);
  }
</style>
</head>
<body>
  <main class="label">
    <div class="frost-border" role="img" aria-label="Frostige Eiskristall-Textur in Weiß und Rosé entlang der Ränder"></div>

    <header class="brand-banner">
      <span class="brand-name">Orvelin</span>
    </header>

    <h1 class="product-title">
      <span class="title-line title-article">THE</span>
      <span class="title-line title-highlight title-highlight--light">VELVET</span>
      <span class="title-line title-highlight title-highlight--deep">DUSK</span>
      <span class="title-line title-tail">MOOD</span>
    </h1>
    <p class="title-line wine-type">Wine</p>
  </main>
</body>
</html>
```